New Branding Business Card Design

Redesign business card according to new branding update.

** The design received so far are single color + BLACK.
I'd encourage designer to use different tones of blue / purple as described in the Designer Brief color palette

Target Market(s)

International

Industry/Entity Type

Medical Equipment

Contact Information for Business Card

Logo on one side (Designer can decide if they want to move certain info from the other side to save space)

Main body info (company name, individual name in both English and Chinese, contact info etc) on the other
Prefer a 'cleaner' layout - vs 'all over the place'
Prefer flush left alignment

Font styles to use
Sans Serif

Requirements
Must have
• Key info
• (Company name (English)): VORAK (HK) Limited
• (Name (English)): Martin L. Osei
• (Credential): FCPA, FHKSI
• (Title): Founder, Managing Director & CEO
• For the following info, designers decide whether to use colon or no colon, stroke separator, or use icon gfx for T (for telephone fixed line, M for mobile etc.)
• T: +852 2741 VORAK / +852 2741 5317
• M: +852 9473 6215 / + 86 139 4527 3916
• E: martin.l.osei@vorak-example.hk
Nice to have
• Depending on the space and spacing available designers can add or use fuller title and other info
• Title: Chairman of the Executive Committee, Founder, Managing Director & CEO
• (Name (Chinese)): 梁文浩
Should not have
• One of our business entities a long company name that cannot be broken into 2 lines
• makes vertical implementation almost impossible

```html
<!DOCTYPE html>
<html lang="en">
<head>
<meta charset="utf-8">
<title>VORAK (HK) Limited – Business Card</title>
<link rel="stylesheet" href="https://fonts.googleapis.com/css2?family=Montserrat:wght@400;500;700&display=swap">
<style>
  :root {
    --purple-deep: #582a84;
    --purple-violet: #6a3fb5;
    --blue-indigo: #3d4fb8;
    --purple-soft: #8f6cc9;
    --ink: #1c1c1c;
    --ink-soft: #3a3a3a;
    --card-white: #ffffff;
    --card-grey: #d7d6d4;
    --backdrop: #eeeeee;
  }
  * { box-sizing: border-box; margin: 0; padding: 0; }
  html, body {
    width: 1200px; height: 1200px; overflow: hidden;
    background: var(--backdrop);
    font-family: "Montserrat", sans-serif;
    color: var(--ink);
  }
  .sheet { position: relative; width: 1200px; height: 1200px; }
  .card {
    position: absolute; left: 170px;
    width: 860px; height: 491px;
    border-radius: 34px;
    box-shadow: 0 6px 18px rgba(0,0,0,0.12);
    overflow: hidden;
  }
  /* Logo side */
  .card--back {
    top: 70px;
    background: var(--card-grey);
    display: flex; align-items: center; justify-content: center;
  }
  .wordmark { display: flex; align-items: center; gap: 22px; }
  .wordmark__square {
    width: 58px; height: 58px; border-radius: 10px;
    background: var(--purple-violet);
  }
  .wordmark__name {
    font-weight: 700; font-size: 72px; letter-spacing: 2px;
    color: var(--purple-deep); line-height: 1;
  }
  /* Info side */
  .card--front { top: 630px; background: var(--card-white); }
  .person { position: absolute; left: 62px; top: 50px; }
  .person__name {
    font-weight: 700; font-size: 32px; letter-spacing: 0.5px;
    color: var(--purple-deep); text-transform: uppercase; line-height: 1.05;
  }
  .person__credentials {
    font-weight: 700; font-size: 15px; margin-top: 6px;
    color: var(--blue-indigo);
  }
  .person__title {
    font-weight: 400; font-size: 15px; margin-top: 2px; color: var(--ink-soft);
  }
  .company {
    position: absolute; left: 62px; top: 200px;
    font-size: 15px; line-height: 1.4; color: var(--ink-soft);
  }
  .company__name {
    font-weight: 700; font-size: 17px; color: var(--purple-violet);
  }
  .contacts { list-style: none; margin-top: 14px; }
  .contact {
    display: flex; align-items: flex-start; gap: 10px;
    font-size: 17px; line-height: 1.3; color: var(--ink);
  }
  .contact__icon {
    width: 16px; height: 18px; flex: none; margin-top: 2px;
    fill: none; stroke: var(--blue-indigo); stroke-width: 1.6;
  }
  .card--front .wordmark {
    position: absolute; right: 56px; bottom: 52px; gap: 16px;
  }
  .card--front .wordmark__square { width: 44px; height: 44px; border-radius: 8px; }
  .card--front .wordmark__name { font-size: 54px; }
  .accent-bar {
    position: absolute; left: 0; top: 0; width: 100%; height: 8px;
    background: linear-gradient(90deg, var(--purple-deep), var(--purple-violet), var(--blue-indigo));
  }
</style>
</head>
<body>
<main class="sheet">
  <section class="card card--back" aria-label="Logo side">
    <div class="wordmark">
      <span class="wordmark__square"></span>
      <span class="wordmark__name">VORAK</span>
    </div>
  </section>

  <section class="card card--front" aria-label="Contact side">
    <div class="person">
      <h1 class="person__name">Martin L. Osei</h1>
      <p class="person__credentials">FCPA, FHKSI</p>
      <p class="person__title">Founder, Managing Director &amp; CEO</p>
    </div>

    <div class="company">
      <h2 class="company__name">VORAK (HK) Limited</h2>
      <p>3rd Floor, Lantern Crest Tower</p>
      <p>18-22 Harbour Lane Street, Central, Hong Kong</p>

      <ul class="contacts">
        <li class="contact">
          <svg class="contact__icon" viewBox="0 0 16 18" aria-hidden="true"><path d="M3 2l3 3-2 2c1 2.5 3 4.5 5 5.5l2-2 3 3-2 2.5C7 15 2 10 .8 4.5z"/></svg>
          <span>+852 2741 VORAK<br>+852 2741 5317</span>
        </li>
        <li class="contact">
          <svg class="contact__icon" viewBox="0 0 16 18" aria-hidden="true"><rect x="4" y="1" width="8" height="16" rx="1.5"/><line x1="7" y1="14.5" x2="9" y2="14.5"/></svg>
          <span>+852 9473 6215<br>+ 86 139 4527 3916</span>
        </li>
        <li class="contact">
          <svg class="contact__icon" viewBox="0 0 16 18" aria-hidden="true"><rect x="1" y="4" width="14" height="11" rx="1"/><path d="M1 5l7 5 7-5"/></svg>
          <span>martin.l.osei@vorak-example.hk</span>
        </li>
      </ul>
    </div>

    <div class="wordmark">
      <span class="wordmark__square"></span>
      <span class="wordmark__name">VORAK</span>
    </div>
  </section>
</main>
</body>
</html>
```